Gum Creek Critters business card and social media card

I would like 2 designs,

one with my logo that I have (attached file) for the front and then the chatterbook, Snapgallery and wanderguide icons on the back.I would like it to be eye catching.

The second design i would like the designers to come up with.I am looking for a colorful and eye catching but easy to read business card. I am in the center of Australia and would like earthy colors like orange/red, yellow, charcoal, brown, green etc. I would like a blue tongue lizard and a king brown snake in the design for the front. For the back I would like the Chatterbook, Snapgallery and wander guide logos.

Industry/Entity Type

Business

Contact Information for Business Card

Marcus Toller
CEO
GUM CREEK CRITTERS pty ltd
W: 041 907 2286
M: 048 216 0947
E: marcus@gumcreekcritters-example.com.au

Font styles to use
Other font styles liked:
• chiller

Colors
f37122
fbed22
ec1f27
474747
0492cd
acd036

Requirements
Must have
• Business name or my logo (attached file)
• Gum Creek Critters (in a cool font, like "chiller")
• Chatterbook icon
• Snapgallery icon
• Wanderguide icon
Nice to have
• Snake and a blue tongue lizard (either the full animals or just the heads)

```html
<!DOCTYPE html>
<html lang="en">
<head>
<meta charset="utf-8">
<title>Gum Creek Critters – Business Card</title>
<link rel="stylesheet" href="https://fonts.googleapis.com/css2?family=Cinzel:wght@600&family=Open+Sans:wght@400;600&display=swap">
<style>
  :root {
    --page: #ecebe8;
    --card-white: #ffffff;
    --brand-red: #c8202f;
    --brand-orange: #f39019;
    --brand-yellow: #e3b021;
    --deep-orange: #f48a1c;
    --charcoal: #333333;
    --pale-scales: #ece4da;
    --lizard-brown: #9c6a4c;
  }
  * { box-sizing: border-box; margin: 0; padding: 0; }
  html, body {
    width: 1200px; height: 900px; overflow: hidden;
    background: var(--page);
    font-family: "Open Sans", Arial, sans-serif;
  }
  .card-sheet {
    position: absolute; inset: 0;
    display: flex; align-items: center; justify-content: center; gap: 40px;
  }
  .card {
    position: relative; width: 530px; height: 303px; overflow: hidden;
    box-shadow: 0 6px 18px rgba(0,0,0,.18);
  }
  /* Front */
  .card--front {
    background: linear-gradient(135deg, var(--deep-orange) 0%, var(--brand-yellow) 55%, var(--deep-orange) 100%);
  }
  .photo-snake {
    position: absolute; left: 0; top: 95px; width: 300px; height: 208px;
    background: radial-gradient(ellipse at 45% 55%, var(--pale-scales) 0%, #d8cfc4 60%, rgba(216,207,196,0) 72%);
  }
  .photo-lizard {
    position: absolute; left: 355px; top: 30px; width: 150px; height: 150px;
    background: radial-gradient(ellipse at 55% 45%, var(--lizard-brown) 0%, #8a6248 50%, rgba(138,98,72,0) 70%);
  }
  /* Back */
  .card--back { background: var(--card-white); }
  .card-wave { position: absolute; inset: 0; width: 100%; height: 100%; }
  .holder { position: absolute; left: 58px; top: 100px; }
  .holder-name {
    font-family: "Cinzel", Georgia, serif; font-weight: 600;
    font-size: 21px; color: var(--brand-red); letter-spacing: .5px;
  }
  .holder-role { font-size: 13px; color: var(--charcoal); margin-top: 2px; }
  .brand-mark {
    position: absolute; right: 28px; top: 30px; width: 170px;
    display: flex; align-items: center; gap: 10px;
  }
  .brand-dot { width: 22px; height: 22px; border-radius: 50%; background: var(--brand-orange); flex: none; }
  .brand-name {
    font-size: 24px; font-weight: 600; line-height: 1.05;
    color: var(--brand-red); text-transform: uppercase;
  }
  .contact-list { position: absolute; left: 58px; top: 160px; list-style: none; }
  .contact-item {
    display: flex; align-items: center; gap: 7px;
    font-size: 13.5px; color: var(--charcoal); line-height: 20px;
  }
  .contact-icon { width: 12px; height: 12px; flex: none; }
  .social-links { position: absolute; right: 16px; top: 212px; display: flex; gap: 5px; }
  .social-tile { width: 24px; height: 24px; border: 2px solid var(--card-white); }
</style>
</head>
<body>
<main class="card-sheet">
  <section class="card card--front" aria-label="Card front">
    <div class="photo-snake" role="img" aria-label="Pale king brown snake coiled across the card"></div>
    <div class="photo-lizard" role="img" aria-label="Blue tongue lizard seen from above"></div>
  </section>

  <section class="card card--back" aria-label="Card back">
    <svg class="card-wave" viewBox="0 0 530 303" preserveAspectRatio="none" aria-hidden="true">
      <path d="M0 262 C240 268 410 250 470 190 C400 262 230 284 0 282 Z" fill="var(--deep-orange)"/>
      <path d="M0 288 C260 290 430 262 530 150 L530 303 L0 303 Z" fill="var(--brand-yellow)" stroke="var(--card-white)" stroke-width="3"/>
    </svg>

    <div class="holder">
      <h1 class="holder-name">Marcus Toller</h1>
      <p class="holder-role">CEO</p>
    </div>

    <div class="brand-mark">
      <span class="brand-dot"></span>
      <span class="brand-name">Gum Creek Critters</span>
    </div>

    <ul class="contact-list">
      <li class="contact-item">
        <svg class="contact-icon" viewBox="0 0 12 12"><path d="M1 4 Q6 0 11 4 L9 5 L8 4 L4 4 L3 5 Z M2 6 H10 L10 11 H2 Z" fill="var(--brand-red)"/></svg>
        041 907 2286
      </li>
      <li class="contact-item">
        <svg class="contact-icon" viewBox="0 0 12 12"><rect x="3" y="0.5" width="6" height="11" rx="1" fill="none" stroke="var(--brand-red)" stroke-width="1.3"/><circle cx="6" cy="9.5" r=".8" fill="var(--brand-red)"/></svg>
        048 216 0947
      </li>
      <li class="contact-item">
        <svg class="contact-icon" viewBox="0 0 12 12"><rect x="0.5" y="2" width="11" height="8" fill="var(--brand-red)"/><path d="M0.5 2 L6 7 L11.5 2" fill="none" stroke="#fff" stroke-width="1"/></svg>
        marcus@gumcreekcritters-example.com.au
      </li>
    </ul>

    <nav class="social-links" aria-label="Chatterbook, Snapgallery, Wanderguide">
      <span class="social-tile"></span>
      <span class="social-tile"></span>
      <span class="social-tile"></span>
    </nav>
  </section>
</main>
</body>
</html>
```